New Zealand Luggage Importer Needs Business Cards

We need professional, creative and fashionable business cards created.
We are based in New Zealand and import and distribute high-end, quality, fashionable and durable luggage.
We pride ourselves on selling the very best quality luggage, second only to 1 brand (which we won't mention here)...we use the same manufacturer. However, our prices are much more reasonable.
Business
Sam Ortiz
027 481 2956
3/17 Kestrel Lane, Morrow Flats, Auckland, 0614
PO Box 208354, North Shore, Auckland 0792
09-527-3061
sales@brindlecases.co.nz / www.brindlecases.co.nz

```html
<!DOCTYPE html>
<html lang="en">
<head>
<meta charset="utf-8">
<title>Brindle Cases – Business Card</title>
<link rel="stylesheet" href="https://fonts.googleapis.com/css2?family=Questrial&display=swap">
<style>
  :root {
    --bg: #d9d6d2;
    --card-black: #030608;
    --card-white: #ffffff;
    --ink: #141414;
    --gold: #c9a45c;
    --logo-light: #ffffff;
  }
  html, body {
    margin: 0;
    width: 1200px;
    height: 1200px;
    overflow: hidden;
    background: var(--bg);
    font-family: "Questrial", sans-serif;
  }
  .canvas { position: relative; width: 1200px; height: 1200px; }
  .card {
    position: absolute;
    left: 311px;
    width: 578px;
    height: 356px;
    box-shadow: 0 3px 10px rgba(0,0,0,0.25);
  }
  .card-back { top: 237px; background: var(--card-black); }
  .card-front { top: 607px; background: var(--card-white); color: var(--ink); }

  .brand-mark {
    position: absolute;
    white-space: nowrap;
    letter-spacing: 0.06em;
  }
  .card-back .brand-mark {
    left: 0; right: 0; top: 158px;
    text-align: center;
    font-size: 34px;
    color: var(--logo-light);
  }
  .card-front .brand-mark {
    right: 57px; top: 48px;
    font-size: 22px;
    color: var(--ink);
  }

  .person-name {
    position: absolute;
    left: 48px; top: 148px;
    font-size: 37px;
    color: var(--gold);
    margin: 0;
    font-weight: 400;
  }
  .dash-rule { position: absolute; left: 278px; top: 165px; }

  .address {
    position: absolute;
    left: 48px;
    width: 170px;
    font-size: 11.5px;
    line-height: 14.5px;
    margin: 0;
  }
  .address-street { top: 238px; padding-bottom: 8px; border-bottom: 1px solid var(--ink); }
  .address-po { top: 290px; }

  .contact-list {
    position: absolute;
    left: 326px; top: 225px;
    list-style: none;
    margin: 0; padding: 0;
    font-size: 13px;
  }
  .contact-list li { display: flex; align-items: center; height: 26px; margin-bottom: 0; }
  .contact-list li:last-child { margin-top: 4px; }
  .contact-list svg { width: 14px; height: 14px; margin-right: 13px; flex: none; }
</style>
</head>
<body>
<div class="canvas">
  <section class="card card-back">
    <div class="brand-mark">BRINDLE CASES</div>
  </section>

  <section class="card card-front">
    <div class="brand-mark">BRINDLE CASES</div>

    <h1 class="person-name">Sam Ortiz</h1>
    <svg class="dash-rule" width="240" height="14" viewBox="0 0 240 14" aria-hidden="true">
      <g fill="var(--gold)">
        <polygon points="4,0 12,0 8,12 0,12"/>
        <polygon points="36,0 44,0 40,12 32,12"/>
        <polygon points="68,0 76,0 72,12 64,12"/>
        <polygon points="100,0 108,0 104,12 96,12"/>
        <polygon points="132,0 140,0 136,12 128,12"/>
        <polygon points="164,0 172,0 168,12 160,12"/>
        <polygon points="196,0 204,0 200,12 192,12"/>
        <polygon points="228,0 236,0 232,12 224,12"/>
      </g>
    </svg>

    <p class="address address-street">3/17 Kestrel Lane, Morrow Flats,<br>Auckland, 0614</p>
    <p class="address address-po">PO Box 208354, North Shore,<br>Auckland 0792</p>

    <ul class="contact-list">
      <li>
        <svg viewBox="0 0 14 14" aria-hidden="true"><rect x="4" y="1" width="6" height="12" rx="1" fill="none" stroke="var(--ink)" stroke-width="1.2"/><rect x="5.5" y="3" width="3" height="4" fill="var(--ink)"/></svg>
        027 481 2956
      </li>
      <li>
        <svg viewBox="0 0 14 14" aria-hidden="true"><path d="M3 1 L5.5 1 L6.5 4 L5 5.5 Q6.5 8.5 8.5 9 L10 7.5 L13 8.5 L13 11 Q12 13 10 13 Q2 11 1 3 Q1 1 3 1 Z" fill="var(--ink)"/></svg>
        09-527-3061
      </li>
      <li>
        <svg viewBox="0 0 14 14" aria-hidden="true"><rect x="1" y="3" width="12" height="8" fill="var(--ink)"/><polyline points="1,3 7,8 13,3" fill="none" stroke="#fff" stroke-width="1"/></svg>
        sales@brindlecases.co.nz
      </li>
      <li>
        <svg viewBox="0 0 14 14" aria-hidden="true"><g fill="none" stroke="var(--ink)" stroke-width="1.1"><circle cx="7" cy="7" r="6"/><ellipse cx="7" cy="7" rx="2.6" ry="6"/><line x1="1" y1="7" x2="13" y2="7"/><line x1="2" y1="4" x2="12" y2="4"/><line x1="2" y1="10" x2="12" y2="10"/></g></svg>
        www.brindlecases.co.nz
      </li>
    </ul>
  </section>
</div>
</body>
</html>
```